Elmrow Management real estate management company needs presentation folder to hand clients

looking for a folder with pockets that represent my real estate management company when i hand to client reports or promotional material. I only do resedential real estate. I want classy and professional - pictures or additioal graphixs are fine

when a client open i will usally insert text and reports about my business
also on the inside flap is usally place for my business card i will upload a picture so the theme can be constant

Target Market(s)

my existing real estate cleints
and i will use when i am soliciting new business

Industry/Entity Type

Real Estate

Font styles to use
Serif

Requirements
Must have
• must have logo
• must give appearance of professionalism and maturity
• have basic company info tel# ,address
• id like viewer to know I manage real estate - focus on residential small to large apartment buildings
• not strip malls, not giganic complexes - im a mid size company
• logo is black but i welcome color as u see fit
Nice to have
• maybe pictures
• my slogan - " we will manage your building like its our own "
• focus on professioanl, safe, trust worthy
• type style should be clear and readable - but im open to sugestions

```html
<!DOCTYPE html>
<html lang="en">
<head>
<meta charset="utf-8">
<title>Elmrow Management Presentation Folder</title>
<link href="https://fonts.googleapis.com/css2?family=Montserrat:wght@400;600;800&display=swap" rel="stylesheet">
<style>
  :root {
    --stage: #b3b3b3;
    --paper: #ffffff;
    --ink: #111111;
    --muted: #555555;
    --sky-light: #e8eef2;
    --sky-mid: #b9cbd6;
    --glass: #8fa9b8;
    --glass-deep: #5e7a8a;
    --crease: #e6e6e6;
    --shadow: rgba(0,0,0,0.28);
  }
  * { box-sizing: border-box; margin: 0; padding: 0; }
  html, body { width: 1200px; height: 960px; overflow: hidden; }
  body {
    background: var(--stage);
    font-family: "Montserrat", Arial, sans-serif;
    color: var(--ink);
    position: relative;
  }

  /* Front cover */
  .cover {
    position: absolute; left: 60px; top: 70px;
    width: 440px; height: 560px;
    background: var(--paper);
    box-shadow: 6px 8px 18px var(--shadow);
    overflow: hidden;
  }
  .cover-photo {
    position: absolute; left: 0; right: 0; bottom: 0; height: 360px;
    background:
      linear-gradient(to bottom, var(--paper) 0%, rgba(255,255,255,0) 45%),
      linear-gradient(100deg, var(--sky-light) 0%, var(--glass) 35%, var(--sky-mid) 55%, var(--glass-deep) 80%, var(--sky-mid) 100%);
  }
  .brand {
    display: flex; align-items: center; gap: 7px;
    font-weight: 800; color: var(--ink); text-transform: uppercase; letter-spacing: 0.5px;
    white-space: nowrap;
  }
  .brand-mark { background: var(--ink); flex: none; }
  .cover-brand { position: absolute; top: 32px; right: 28px; font-size: 13px; }
  .cover-brand .brand-mark { width: 14px; height: 14px; }
  .cover-footer { position: absolute; left: 24px; bottom: 30px; }
  .footer-brand { font-size: 9px; margin-bottom: 8px; }
  .footer-brand .brand-mark { width: 9px; height: 9px; }
  .contact-line { font-size: 6.5px; color: var(--muted); line-height: 1.6; font-weight: 400; white-space: nowrap; }
  .cover-slogan {
    position: absolute; left: 186px; bottom: 58px;
    font-size: 15px; font-weight: 800; line-height: 1.55;
    white-space: nowrap;
  }

  /* Inside spread */
  .spread {
    position: absolute; left: 620px; top: 440px;
    width: 540px; height: 430px;
    display: flex;
    filter: drop-shadow(6px 8px 12px var(--shadow));
  }
  .panel {
    position: relative; width: 270px; height: 100%;
    background: var(--paper);
  }
  .panel-left { border-right: 1px solid var(--crease); }
  .side-flap {
    position: absolute; top: 14px; bottom: 14px; width: 12px;
    border: 1px solid var(--crease); background: var(--paper);
  }
  .panel-left .side-flap { left: 8px; }
  .panel-right .side-flap { right: 8px; }
  .flap-notch {
    position: absolute; top: 45%; width: 18px; height: 26px;
    border: 1px solid var(--crease); border-radius: 50%; background: var(--paper);
  }
  .panel-left .flap-notch { left: 4px; }
  .panel-right .flap-notch { right: 4px; }
  .pocket {
    position: absolute; left: 6px; right: 6px; bottom: 0; height: 150px;
    background: var(--paper);
    border-top: 1px solid var(--crease);
    box-shadow: 0 -3px 6px rgba(0,0,0,0.08);
  }
  .panel-left .pocket { border-top-right-radius: 40px; }
  .panel-right .pocket { border-top-left-radius: 40px; }
  .pocket-brand { position: absolute; left: 50%; top: 42px; transform: translateX(-50%); font-size: 12px; }
  .pocket-brand .brand-mark { width: 12px; height: 12px; }
  .pocket-slogan {
    position: absolute; left: 0; right: 0; top: 78px;
    text-align: center; font-size: 8px; font-weight: 800; line-height: 1.5;
  }
  .business-card {
    position: absolute; left: 50%; top: 38px; transform: translateX(-50%);
    width: 140px; height: 80px;
    background: var(--paper); border: 3px solid var(--ink);
    padding: 8px 8px; display: flex; gap: 6px;
  }
  .card-mark { width: 24px; height: 24px; background: var(--ink); flex: none; }
  .card-name { font-size: 8.5px; font-weight: 800; white-space: nowrap; }
  .card-detail { font-size: 4.5px; color: var(--muted); line-height: 1.55; white-space: nowrap; }
  .card-slit { position: absolute; width: 12px; height: 2px; background: var(--ink); }
</style>
</head>
<body>

  <section class="cover">
    <div class="cover-photo" role="img" aria-label="Soft-focus photograph of glass residential and office towers against a pale sky"></div>
    <div class="brand cover-brand"><span class="brand-mark"></span>Elmrow Management</div>
    <p class="cover-slogan">We Will Manage Your Building<br>Like Its Our Own</p>
    <div class="cover-footer">
      <div class="brand footer-brand"><span class="brand-mark"></span>Elmrow Management</div>
      <p class="contact-line">(555) 014-2290 &nbsp;(555) 014-2291 &nbsp;hello@elmrowmgmt.com</p>
      <p class="contact-line">Unit 412, 9 Linden Row &nbsp;Ashford WK 5021</p>
    </div>
  </section>

  <section class="spread">
    <div class="panel panel-left">
      <div class="side-flap"><span class="flap-notch"></span></div>
      <div class="pocket">
        <div class="brand pocket-brand"><span class="brand-mark"></span>Elmrow Management</div>
        <p class="pocket-slogan">We Will Manage Your Building<br>Like Its Our Own</p>
      </div>
    </div>
    <div class="panel panel-right">
      <div class="side-flap"><span class="flap-notch"></span></div>
      <div class="pocket">
        <div class="business-card">
          <span class="card-slit" style="left:-8px;top:-4px;transform:rotate(45deg)"></span>
          <span class="card-slit" style="right:-8px;top:-4px;transform:rotate(-45deg)"></span>
          <span class="card-slit" style="left:-8px;bottom:-4px;transform:rotate(-45deg)"></span>
          <span class="card-slit" style="right:-8px;bottom:-4px;transform:rotate(45deg)"></span>
          <span class="card-mark"></span>
          <div>
            <p class="card-name">Daniel Harlow</p>
            <p class="card-detail">Residential Property Manager</p>
            <p class="card-detail">office 555 014 2290</p>
            <p class="card-detail">email dh@elmrowmgmt.com</p>
            <p class="card-detail">cell 555 014 2295</p>
            <p class="card-detail">9 Linden Row, Ashford</p>
          </div>
        </div>
      </div>
    </div>
  </section>

</body>
</html>
```